Business Card Design Project

We are a construction company in Orange County, CA. We need a two sided business card. We would like the back to be our logo with web URL. Front should included Name, title, address, phone, fax and email address.

our address is
387 West Marlowe Blvd, Suite 402
Westbrook, CA 90417

Our logo files are attached.

Construction

```html
<!DOCTYPE html>
<html lang="en">
<head>
<meta charset="utf-8">
<title>Keston Business Card</title>
<link href="https://fonts.googleapis.com/css2?family=Archivo+Black&family=Roboto:wght@400;500;700&display=swap" rel="stylesheet">
<style>
  :root {
    --stage: #eceef0;
    --blue-light: #3fb3dc;
    --blue-mid: #1f86c2;
    --blue-deep: #0d5d9c;
    --logo-blue: #1a5fa3;
    --white: #ffffff;
    --card-shadow: rgba(10, 40, 70, 0.25);
  }
  * { margin: 0; padding: 0; box-sizing: border-box; }
  html, body { width: 1200px; height: 902px; overflow: hidden; background: var(--stage); }
  .stage {
    width: 1200px; height: 902px;
    display: flex; align-items: center; justify-content: center; gap: 60px;
    font-family: "Roboto", Arial, sans-serif;
  }
  .card {
    position: relative;
    width: 520px; height: 297px;
    border-radius: 18px;
    overflow: hidden;
    box-shadow: 0 10px 28px var(--card-shadow);
    background: linear-gradient(135deg, var(--blue-light) 0%, var(--blue-mid) 52%, var(--blue-deep) 100%);
  }
  .front-white {
    position: absolute; left: 0; top: 0;
    width: 100%; height: 150px;
    background: var(--white);
  }
  .wordmark {
    position: absolute;
    font-family: "Archivo Black", "Arial Black", sans-serif;
    letter-spacing: 2px;
    line-height: 1;
  }
  .card-back .wordmark { left: 0; right: 0; top: 104px; text-align: center; font-size: 78px; color: var(--white); }
  .back-url {
    position: absolute; right: 26px; bottom: 22px;
    color: var(--white); font-size: 17px; letter-spacing: 0.5px;
  }
  .card-front .wordmark { left: 34px; top: 44px; font-size: 70px; color: var(--logo-blue); }
  .holder { position: absolute; left: 28px; bottom: 26px; color: var(--white); }
  .holder-name { font-size: 17px; font-weight: 700; letter-spacing: 0.5px; }
  .holder-title { font-size: 14px; margin-top: 3px; }
  .contact {
    position: absolute; right: 24px; bottom: 20px;
    list-style: none; text-align: right;
    color: var(--white); font-size: 11.5px; line-height: 1.6;
  }
  .contact svg { width: 10px; height: 10px; margin-left: 6px; vertical-align: -1px; fill: var(--white); }
</style>
</head>
<body>
<main class="stage">
  <section class="card card-back" aria-label="Card back">
    <div class="wordmark">KESTON</div>
    <div class="back-url">www.kestonbuild.com</div>
  </section>

  <section class="card card-front" aria-label="Card front">
    <div class="front-white"></div>
    <div class="wordmark">KESTON</div>
    <div class="holder">
      <div class="holder-name">DALE MERCER</div>
      <div class="holder-title">President</div>
    </div>
    <ul class="contact">
      <li>387 West Marlowe Blvd, Suite 402<svg viewBox="0 0 10 10"><path d="M5 0a3.5 3.5 0 0 0-3.5 3.5C1.5 6 5 10 5 10s3.5-4 3.5-6.5A3.5 3.5 0 0 0 5 0zm0 5a1.5 1.5 0 1 1 0-3 1.5 1.5 0 0 1 0 3z"/></svg></li>
      <li>Westbrook, CA 90417<svg viewBox="0 0 10 10"></svg></li>
      <li>555.214.0142<svg viewBox="0 0 10 10"><path d="M2 0l2 2.5-1 1.2a6 6 0 0 0 3.3 3.3l1.2-1L10 8l-1.3 2C4 10 0 6 0 1.3z"/></svg></li>
      <li>555.214.0187<svg viewBox="0 0 10 10"><rect x="1" y="3" width="8" height="5"/><rect x="3" y="0.5" width="4" height="2.5"/></svg></li>
      <li>dmercer@kestonbuild.com<svg viewBox="0 0 10 10"><path d="M0 2h10v6H0z M0 2l5 3.5L10 2" stroke="#1f86c2" stroke-width="0.8"/></svg></li>
      <li>www.kestonbuild.com<svg viewBox="0 0 10 10"><circle cx="5" cy="5" r="4.5"/></svg></li>
    </ul>
  </section>
</main>
</body>
</html>
```